Summit In Boots Flyer, eyecatching

Hi,
To give you an idea of the business for design purposes, #SummitttInBoots is predominantly a recruitment and people development business, ran by me dedicated to training & assisting others in achieving extra income (pt or f/t) around their current commitments, people also have the opportunity to build their own business brand with my support. My brand colours are Red, White and Black, and I would like to incorporate the following text;

#SummitInBoots

Recruiting now! Start today & start earning!

Would you like an extra income, for…
A holiday?…A new car?…Lifestyle changes?
(Can you put a tick box or something similar adjacent to each)

Are you facing…
Redundancy? Birth of a new child? Hefty bills?

If so, I have the solution.

Contact Rosalind Pawley today: (can you insert the appropriate icon for each of the contact details)
Tel: 07941 608274
Twitter: @Summit_InBoots
Email: Rosalind@summitinboots-example.co.uk
Facebook: www.linkpage-example.com/rosandsummitinboots

Target Market(s)

Women aged 25-45 years, possibly busy mums too, wanting to earn additinal income to allow them more choices, be it family time, money, new challenge, meeting new people, personal development

Industry/Entity Type

Health And Wellness

Font styles to use
Serif
Sans Serif
Decorative
Script

Colors
ec1f27
ffffff
000000

Requirements
Must have
• My heels logo, be clear concise and eye catching, I also have the following strap line if you wish to use;
• Empowering other to achieve
• Also I have attached a closeup picture of myself but would ideally only like half my face to appear (leftside) similar to the other picture posted - if you can
Nice to have
• Perhaps adding other forms of graphics, or the 3rd picture I have attached with myself...possibly just the shoes though
Should not have
• Too many colours

```html
<!DOCTYPE html>
<html lang="en">
<head>
<meta charset="utf-8">
<title>Summit In Boots – Recruiting Flyer</title>
<link rel="stylesheet" href="https://fonts.googleapis.com/css2?family=Roboto:wght@400;500;700&family=Play:wght@400;700&display=swap">
<style>
  :root {
    --red: #ec1f27;
    --red-deep: #c8141b;
    --ink: #000000;
    --bar: #2f2f31;
    --white: #ffffff;
    --paper: #f2f2f2;
    --text-grey: #3a3a3a;
    --ring: #f1a99a;
    --stage: #e9e6e2;
  }
  * { margin: 0; padding: 0; box-sizing: border-box; }
  html, body { width: 825px; height: 1200px; overflow: hidden; }
  body { background: var(--stage); position: relative; font-family: "Roboto", Arial, sans-serif; }

  .flyer {
    position: absolute; left: 87px; top: 138px;
    width: 652px; height: 919px;
    background: linear-gradient(180deg, var(--white) 0%, var(--paper) 100%);
    overflow: hidden;
    box-shadow: 0 6px 18px rgba(0,0,0,.25);
  }
  .flyer-shapes { position: absolute; inset: 0; }

  .headline { position: absolute; left: 42px; top: 36px; }
  .headline-title { color: var(--red); font-weight: 700; font-size: 37px; letter-spacing: -0.2px; line-height: 1; }
  .headline-sub { color: var(--text-grey); font-family: "Play", "Roboto", sans-serif; font-size: 20px; margin-top: 5px; letter-spacing: 0.3px; }

  .hashtag-bar {
    position: absolute; left: 0; top: 119px; width: 311px; height: 48px;
    background: var(--bar); color: var(--white);
    font-size: 28px; font-weight: 500; line-height: 48px; padding-left: 34px;
  }

  .brand-badge {
    position: absolute; left: 59px; top: 213px; width: 220px; height: 220px;
    border-radius: 50%; background: var(--white);
    border: 9px solid var(--ring);
    box-shadow: 0 0 0 3px var(--white);
    display: flex; align-items: center; justify-content: center; text-align: center;
  }
  .brand-name { font-size: 28px; font-weight: 700; color: var(--ink); line-height: 1.15; }

  .name-bar {
    position: absolute; left: 40px; top: 482px; width: 245px; height: 40px;
    background: var(--bar); color: var(--white);
    font-size: 20px; font-weight: 500; line-height: 40px; text-align: center;
  }

  .contact-block { position: absolute; left: 64px; top: 762px; color: var(--white); }
  .contact-title { font-size: 19px; font-weight: 700; letter-spacing: 0.3px; }
  .contact-line { display: flex; align-items: center; gap: 6px; margin-top: 4px; }
  .contact-phone { font-size: 24px; font-weight: 700; letter-spacing: 0.5px; }
  .contact-handle { font-size: 18px; }
  .handle-dot { width: 12px; height: 12px; border-radius: 50%; background: var(--white); display: inline-block; margin-right: 3px; }

  .question-bar {
    position: absolute; left: 309px; width: 343px; height: 26px;
    background: var(--bar); color: var(--white);
    font-size: 14.5px; font-weight: 700; line-height: 26px; padding-left: 11px;
  }
  .question-bar.income { top: 546px; }
  .question-bar.facing { top: 680px; }

  .checklist { position: absolute; left: 323px; list-style: none; font-family: "Play", "Roboto", sans-serif; }
  .checklist.income { top: 581px; }
  .checklist.facing { top: 720px; }
  .checklist li {
    font-size: 21px; color: var(--text-grey); letter-spacing: 1px;
    height: 27px; line-height: 27px; display: flex; align-items: center;
  }
  .checkbox { width: 14px; height: 14px; border: 1.5px solid var(--red); margin-right: 14px; flex: none; }

  .solution { position: absolute; left: 318px; top: 816px; color: var(--red); font-weight: 700; font-size: 27px; font-family: "Play", "Roboto", sans-serif; }

  .footer-rule { position: absolute; left: 0; top: 868px; width: 652px; height: 4px; background: var(--red); }
  .footer-bar {
    position: absolute; left: 0; top: 874px; width: 652px; height: 45px;
    background: var(--bar); color: var(--white);
    display: flex; align-items: center; justify-content: center; gap: 6px;
    font-size: 13.5px; white-space: nowrap; font-family: Arial, "Roboto", sans-serif;
  }
  .footer-bar .divider { margin: 0 4px; }
  .footer-square { width: 9px; height: 9px; background: var(--red); display: inline-block; }
</style>
</head>
<body>
<div class="flyer">
  <svg class="flyer-shapes" width="652" height="919" viewBox="0 0 652 919">
    <defs>
      <linearGradient id="portraitTone" x1="0" y1="0" x2="1" y2="1">
        <stop offset="0" stop-color="#f6e6dc"/>
        <stop offset="0.5" stop-color="#e6b9a8"/>
        <stop offset="1" stop-color="#5a4a48"/>
      </linearGradient>
      <linearGradient id="snapTone" x1="0" y1="0" x2="1" y2="0">
        <stop offset="0" stop-color="#3a3a3a"/>
        <stop offset="0.5" stop-color="#d9c7c0"/>
        <stop offset="1" stop-color="#e8c2b4"/>
      </linearGradient>
      <linearGradient id="panelRed" x1="0" y1="0" x2="1" y2="0">
        <stop offset="0" stop-color="var(--red-deep)"/>
        <stop offset="0.5" stop-color="var(--red)"/>
        <stop offset="1" stop-color="var(--red-deep)"/>
      </linearGradient>
    </defs>
    <!-- portrait area -->
    <path d="M284 0 H652 V460 C652 486 636 502 610 502 H284 Z" fill="url(#portraitTone)" role="img" aria-label="Close-up portrait photograph of the business owner"/>
    <!-- left red edge and sweeping curve -->
    <rect x="0" y="0" width="28" height="119" fill="var(--red)"/>
    <rect x="24" y="167" width="6" height="240" fill="var(--red)"/>
    <path d="M24 400 C20 470 60 512 140 512 H652 V519 H140 C50 519 10 470 14 400 Z" fill="var(--red)"/>
    <path d="M30 400 C30 466 66 505 140 505 H612 C636 505 650 490 651 468" fill="none" stroke="var(--ink)" stroke-width="3"/>
    <!-- red panel -->
    <path d="M40 867 V320 A122 122 0 0 1 285 320 V867 Z" fill="url(#panelRed)"/>
    <!-- small photo -->
    <rect x="68" y="555" width="188" height="168" rx="14" fill="var(--white)"/>
    <rect x="73" y="560" width="178" height="158" rx="11" fill="url(#snapTone)" role="img" aria-label="Pair of photographs of the business owner"/>
  </svg>

  <div class="headline">
    <p class="headline-title">Recruiting now!</p>
    <p class="headline-sub">Start today &amp; start earning!</p>
  </div>

  <div class="hashtag-bar">#SummitInBoots</div>

  <div class="brand-badge"><span class="brand-name">Summit<br>In Boots</span></div>

  <div class="name-bar">Rosalind Pawley</div>

  <div class="contact-block">
    <p class="contact-title">CONTACT TODAY!</p>
    <p class="contact-line contact-phone">
      <svg width="16" height="20" viewBox="0 0 16 20"><path d="M4 1 L7 5 L5 7 C6 10 7 12 9 14 L11 12 L15 15 L12 19 C6 18 1 11 1 4 Z" fill="var(--white)"/></svg>
      07941 608274
    </p>
    <p class="contact-line contact-handle"><span class="handle-dot"></span>@Summit_InBoots</p>
  </div>

  <div class="question-bar income">Would you like an extra income, for...</div>
  <ul class="checklist income">
    <li><span class="checkbox"></span>A holiday?</li>
    <li><span class="checkbox"></span>A new car?</li>
    <li><span class="checkbox"></span>Lifestyle changes?</li>
  </ul>

  <div class="question-bar facing">Are you facing...</div>
  <ul class="checklist facing">
    <li><span class="checkbox"></span>Redundancy?</li>
    <li><span class="checkbox"></span>Birth of a new child?</li>
    <li><span class="checkbox"></span>Hefty bills?</li>
  </ul>

  <p class="solution">If so, I have the solution</p>

  <div class="footer-rule"></div>
  <div class="footer-bar">
    <svg width="14" height="10" viewBox="0 0 14 10"><rect x="0.5" y="0.5" width="13" height="9" fill="var(--red)"/><path d="M0.5 0.5 L7 6 L13.5 0.5" fill="none" stroke="var(--bar)" stroke-width="1.2"/></svg>
    <span>Rosalind@summitinboots-example.co.uk</span>
    <span class="divider">|</span>
    <span class="footer-square"></span>
    <span>www.linkpage-example.com/rosandsummitinboots</span>
  </div>
</div>
</body>
</html>
```